Design Creative Business Cards for an Education Company

***CONTEST HAS CHANGED!!*******ITS NOW FOR A CLEANING COMPANY***
****FINAL FILES MUST BE SUBMITTED AS PSD LAYERED FILES WITH EDITABLE TEXT (300dpi, CMYK color)****

Cards should be standard US size (2" X 3.5" with 1/8" bleed on each side)

create nice creative cards using the attached logo and the information below:

Mira Talbeck
www brightandnimble.example
716-555-4827
brightandnimble716@mailbox.example

```html
<!DOCTYPE html>
<html lang="en">
<head>
<meta charset="utf-8">
<title>Bright and Nimble — Business Cards</title>
<link rel="stylesheet" href="https://fonts.googleapis.com/css2?family=Open+Sans:wght@400;700&display=swap">
<style>
  :root {
    --backdrop: #a9d3ac;
    --card-grey: #d6d6d8;
    --card-white: #ffffff;
    --sky-blue: #3a97d4;
    --deep-blue: #2b5fa6;
    --teal: #2fb3bd;
    --brand-teal: #2aa0aa;
    --ink-white: #ffffff;
    --icon-dark: #1d2e44;
  }
  * { margin: 0; padding: 0; box-sizing: border-box; }
  html, body {
    width: 1200px;
    height: 900px;
    overflow: hidden;
    background: var(--backdrop);
    font-family: "Open Sans", sans-serif;
  }
  .sheet {
    position: relative;
    width: 1200px;
    height: 900px;
    display: flex;
    flex-direction: column;
    align-items: center;
    justify-content: center;
    gap: 60px;
  }
  .card {
    position: relative;
    width: 630px;
    height: 360px;
    overflow: hidden;
    box-shadow: 0 6px 18px rgba(0, 0, 0, 0.18);
  }
  .card-art {
    position: absolute;
    inset: 0;
    width: 100%;
    height: 100%;
  }

  /* Front: name and contacts */
  .holder-name {
    position: absolute;
    left: 56px;
    top: 128px;
    color: var(--ink-white);
    font-weight: 700;
    font-size: 30px;
    letter-spacing: 0.5px;
    padding-bottom: 8px;
    border-bottom: 3px solid var(--ink-white);
  }
  .contact-list {
    position: absolute;
    left: 362px;
    top: 120px;
    width: 246px;
    list-style: none;
    display: flex;
    flex-direction: column;
    gap: 18px;
  }
  .contact-item {
    display: flex;
    align-items: center;
    gap: 8px;
    color: var(--ink-white);
    font-size: 11px;
    line-height: 1.2;
    white-space: nowrap;
  }
  .contact-icon {
    width: 20px;
    height: 20px;
    flex: none;
  }

  /* Back: brand */
  .brand {
    position: absolute;
    left: 0;
    right: 0;
    top: 140px;
    display: flex;
    align-items: center;
    justify-content: center;
    gap: 12px;
  }
  .brand-dot {
    width: 22px;
    height: 22px;
    border-radius: 50%;
    background: var(--brand-teal);
  }
  .brand-name {
    color: var(--brand-teal);
    font-weight: 400;
    font-size: 26px;
    letter-spacing: 3px;
    text-transform: uppercase;
  }
</style>
</head>
<body>
<main class="sheet">

  <section class="card card-front" aria-label="Business card front">
    <svg class="card-art" viewBox="0 0 630 360" aria-hidden="true">
      <rect width="630" height="360" fill="var(--card-grey)"/>
      <polygon points="0,0 64,0 0,160" fill="var(--sky-blue)"/>
      <polygon points="330,0 630,0 630,360 378,360" fill="var(--sky-blue)"/>
      <polygon points="470,0 630,0 630,150" fill="var(--deep-blue)"/>
    </svg>

    <h1 class="holder-name">Mira Talbeck</h1>

    <ul class="contact-list">
      <li class="contact-item">
        <svg class="contact-icon" viewBox="0 0 20 20" aria-hidden="true">
          <circle cx="10" cy="10" r="10" fill="var(--icon-dark)"/>
          <path d="M6.5 5.5 L8.5 5.5 L9.3 8 L8.2 9 Q9.3 11 11 11.8 L12 10.7 L14.5 11.5 L14.5 13.5 Q10 14 7.6 11.6 Q5.5 9.4 6.5 5.5 Z" fill="var(--ink-white)"/>
        </svg>
        <span>716-555-4827</span>
      </li>
      <li class="contact-item">
        <svg class="contact-icon" viewBox="0 0 20 20" aria-hidden="true">
          <circle cx="10" cy="10" r="10" fill="var(--icon-dark)"/>
          <rect x="5" y="6.5" width="10" height="7" fill="none" stroke="var(--ink-white)" stroke-width="1.3"/>
          <polyline points="5,6.5 10,10.5 15,6.5" fill="none" stroke="var(--ink-white)" stroke-width="1.3"/>
        </svg>
        <span>brightandnimble716@mailbox.example</span>
      </li>
      <li class="contact-item">
        <svg class="contact-icon" viewBox="0 0 20 20" aria-hidden="true">
          <circle cx="10" cy="10" r="10" fill="var(--icon-dark)"/>
          <circle cx="10" cy="10" r="5" fill="none" stroke="var(--ink-white)" stroke-width="1.2"/>
          <ellipse cx="10" cy="10" rx="2.2" ry="5" fill="none" stroke="var(--ink-white)" stroke-width="1"/>
          <line x1="5" y1="10" x2="15" y2="10" stroke="var(--ink-white)" stroke-width="1"/>
        </svg>
        <span>www brightandnimble.example</span>
      </li>
    </ul>
  </section>

  <section class="card card-back" aria-label="Business card back">
    <svg class="card-art" viewBox="0 0 630 360" aria-hidden="true">
      <rect width="630" height="360" fill="var(--card-grey)"/>
      <polygon points="330,276 630,226 630,268 390,268" fill="var(--teal)"/>
      <polygon points="0,318 390,268 630,268 630,360 0,360" fill="var(--card-white)"/>
    </svg>

    <div class="brand">
      <span class="brand-dot" aria-hidden="true"></span>
      <span class="brand-name">Bright and Nimble</span>
    </div>
  </section>

</main>
</body>
</html>
```